Create a Flyer for a Darts Tournament

We need a Flyer for a Darts Tournament that is going to be organized by our darts department (logo attached). The name of the tournament is "3. KLW Dartsturnier". The Flyer should look modern, professional and in a way that everyone can see at the first impression that is has to do with dart sports. The logo of our department should be on the flyer as well. On the flyer we need an area where we can place some informations regarding the tournament (bullet points) etc. And a area where we can place informations regarding the registration progress (e.g. "Registration via E-Mail". Should fit well to our logo.

Target Market(s)

Darts Players for the Tournament

Font styles to use
Serif

Colors

Designer to choose colors to be used in the design.

Requirements
Must have
• Name of the Tournament, our Logo, place for some tournament details, link to our registration page (besucher.tv-hallwitz.de). Should

```html
<!DOCTYPE html>
<html lang="de">
<head>
<meta charset="utf-8">
<title>3. KLW Dartsturnier – Flyer</title>
<link rel="stylesheet" href="https://fonts.googleapis.com/css2?family=Montserrat:wght@400;500;700;800;900&display=swap">
<style>
  :root{
    --stage:#e4e4e4;
    --black:#000;
    --navy:#0b3a78;
    --blue:#0a5cb8;
    --blue-bright:#1f7fe6;
    --ink-blue:#0b3d73;
    --ice:#bfe0ff;
    --white:#fff;
    --grey-logo:#7d7d7d;
    --grey-band:#b9b9b9;
    --grey-light:#d8d8d8;
    --grey-pill:#8a8a8a;
    --text-dark:#1d1d1d;
  }
  *{box-sizing:border-box;margin:0;padding:0}
  html,body{width:944px;height:1200px;overflow:hidden}
  body{background:var(--stage);font-family:"Montserrat",sans-serif;position:relative}
  .flyer{position:absolute;left:44px;top:0;width:856px;height:1200px;background:var(--black);overflow:hidden}
  .flyer > *{position:absolute}

  .hero-photo{left:0;top:0;width:856px;height:495px;
    background:radial-gradient(ellipse at 28% 45%,#4a4a4a 0%,#1d1d1d 38%,#050505 70%),#000}
  .logo-box{left:619px;top:0;width:213px;height:221px;background:var(--grey-logo);
    display:flex;flex-direction:column;align-items:center;justify-content:center;gap:10px}
  .logo-dot{width:54px;height:54px;border-radius:50%;background:var(--white)}
  .logo-name{font-weight:800;font-size:30px;color:var(--white);letter-spacing:1px}

  .title-panel{left:0;top:495px;width:469px;height:262px;
    background:linear-gradient(90deg,var(--navy) 0%,var(--blue) 100%)}
  .edition{left:58px;top:520px;font-weight:900;font-size:196px;line-height:1;color:var(--white);
    text-shadow:0 0 6px var(--blue-bright),0 0 14px var(--blue-bright),0 0 26px #3b9bff}
  .title-rule{left:187px;top:538px;width:1px;height:142px;background:rgba(255,255,255,.7)}
  .club{left:193px;top:527px;font-weight:500;font-size:94px;line-height:1;color:var(--white);letter-spacing:-1px}
  .event{left:195px;top:619px;font-weight:700;font-size:30px;line-height:1;color:var(--white);letter-spacing:-.3px}
  .restriction{left:195px;top:659px;width:233px;height:33px;background:#ececec;
    color:var(--blue);font-size:18px;font-weight:500;display:flex;align-items:center;justify-content:center}
  .restriction b{font-weight:800;margin-right:5px}
  .format{left:57px;top:707px;width:371px;height:34px;border-top:1px solid rgba(255,255,255,.8);
    border-bottom:1px solid rgba(255,255,255,.8);display:flex;align-items:center;justify-content:space-between;
    font-size:22px;color:var(--ice);white-space:nowrap}
  .format b{font-weight:800}

  .date-panel{left:469px;top:495px;width:387px;height:285px;background:var(--white)}
  .day-number{left:541px;top:526px;font-weight:900;font-size:152px;line-height:1;color:var(--blue);letter-spacing:-4px}
  .day-suffix{left:750px;top:537px;font-weight:700;font-size:32px;color:var(--blue)}
  .weekday{left:544px;top:664px;font-weight:900;font-size:36px;line-height:1;color:var(--blue)}
  .month-year{left:507px;top:706px;width:296px;height:35px;border-top:1px solid var(--blue);border-bottom:1px solid var(--blue);
    display:flex;align-items:center;justify-content:center;font-weight:800;font-size:21px;color:var(--ink-blue)}

  .info-band{left:0;top:780px;width:856px;height:171px;background:var(--grey-band)}
  .venue{left:0;top:758px;width:641px;height:47px;border-radius:0 24px 24px 0;
    background:linear-gradient(90deg,#6f6f6f,#9a9a9a);color:var(--white);font-weight:900;font-size:27px;
    display:flex;align-items:center;padding-left:56px;text-shadow:0 2px 3px rgba(0,0,0,.5);white-space:nowrap}
  .details{top:838px;font-size:21px;line-height:27px;color:var(--text-dark);list-style:none;white-space:nowrap}
  .details b{font-weight:800;color:var(--ink-blue)}
  .details-left{left:47px}
  .details-right{left:443px}
  .details-rule{left:402px;top:831px;width:2px;height:106px;background:#222}

  .notes-area{left:0;top:951px;width:856px;height:156px;background:var(--grey-light)}
  .footer{left:0;top:1107px;width:856px;height:93px;background:var(--black)}
  .registration{left:111px;top:1087px;width:634px;height:50px;border-radius:25px;overflow:hidden;
    background:linear-gradient(180deg,#e0e0e0,#9d9d9d);display:flex;align-items:center}
  .registration-label{width:233px;height:100%;border-radius:25px 0 0 25px;
    background:linear-gradient(180deg,var(--blue-bright),var(--navy));color:var(--white);font-weight:900;font-size:25px;
    display:flex;align-items:center;justify-content:center;text-shadow:0 2px 3px rgba(0,0,0,.5)}
  .registration-url{padding-left:10px;font-size:22px;color:#111;white-space:nowrap}
  .registration-url b{font-weight:900;margin-right:6px}
  .info-link{left:0;top:1141px;width:856px;text-align:center;color:var(--white);font-size:19px}
  .info-link span{border-bottom:1px solid var(--white);padding-bottom:3px}
  .info-link b{font-weight:700}
</style>
</head>
<body>
<main class="flyer">
  <div class="hero-photo" role="img" aria-label="Schwarzweißfoto: Dartspieler wirft auf eine Steel-Dartscheibe"></div>
  <div class="logo-box">
    <div class="logo-dot"></div>
    <div class="logo-name">KLW Darts</div>
  </div>

  <div class="title-panel"></div>
  <div class="edition">3</div>
  <div class="title-rule"></div>
  <div class="club">KLW</div>
  <div class="event">DARTSTURNIER</div>
  <div class="restriction"><b>KEINE</b> LIGASPIELER</div>
  <div class="format"><span><b>STEEL DARTS</b> HOBBYTURNIER</span></div>

  <div class="date-panel"></div>
  <div class="day-number">25</div>
  <div class="day-suffix">th</div>
  <div class="weekday">SONNTAG</div>
  <div class="month-year">JANUARY | 2025</div>

  <div class="info-band"></div>
  <div class="venue">SPORTHALLE IN 04567 HALLWITZ</div>
  <ul class="details details-left">
    <li><b>SAMSTAG</b> 25.01.2025</li>
    <li><b>EINLASS</b> 16:00 UHR</li>
    <li><b>TURNIERBEGINN</b> 17:00 UHR</li>
  </ul>
  <div class="details-rule"></div>
  <ul class="details details-right">
    <li><b>MAXIMAL</b> 48 TEILNEHMER</li>
    <li><b>GRUPPENPHASE</b> 301 | DO | BO3</li>
    <li><b>KO-PHASE</b> 501 | DO | BO5</li>
  </ul>

  <div class="notes-area"></div>
  <div class="footer"></div>
  <div class="registration">
    <div class="registration-label">ANMELDUNG</div>
    <div class="registration-url"><b>:</b>BESUCHER.TV-HALLWITZ.DE</div>
  </div>
  <div class="info-link"><span><b>INFOS:</b> DARTS.TV-HALLWITZ.DE</span></div>
</main>
</body>
</html>
```